Photojournalism/photography business needs a simple, timeless & professional letterhead design

We need a letterhead design for photography/photojournalism business called 'plomk', no capitals.

The letterhead needs to be:
- simple
- professional
- timeless
- easy to read
- consists of at least 2 colors to make it stands out.

We do mainly editorial photography, photo articles for various publications, travel, businesses, as well as people such as family and kids.

The final design should communicate professionalism, easy identification, attention grabbing, even if it has to be found among a stack of various papers on the clients' desks.

Target Market(s)

Various publications.

Industry/Entity Type

Business

Requirements
Must have
• Please use the logo attached.

```html
<!DOCTYPE html>
<html lang="en">
<head>
<meta charset="utf-8">
<title>plomk letterhead</title>
<link rel="stylesheet" href="https://fonts.googleapis.com/css2?family=Open+Sans:ital,wght@0,400;0,700;1,400&family=Cormorant+Garamond:ital,wght@1,500&display=swap">
<style>
  :root {
    --backdrop: #e6e3de;
    --paper: #ffffff;
    --brand-red: #e31e2a;
    --ink: #3a3a3a;
    --ink-soft: #555555;
    --panel-grey: #f3f3f5;
    --watermark: #e4e4e8;
  }
  * { box-sizing: border-box; margin: 0; padding: 0; }
  html, body { width: 1200px; height: 1024px; overflow: hidden; }
  body {
    background: var(--backdrop);
    font-family: "Open Sans", Arial, sans-serif;
    color: var(--ink);
    position: relative;
  }
  .letterhead {
    position: absolute;
    left: 260px; top: 31px;
    width: 680px; height: 962px;
    background: var(--paper);
    box-shadow: 0 6px 24px rgba(0,0,0,.18);
    overflow: hidden;
  }
  .brand-name {
    position: absolute;
    left: 262px; top: 44px;
    font-size: 58px; font-weight: 700;
    color: var(--brand-red);
    letter-spacing: -1px;
    line-height: 1;
  }
  .sender {
    position: absolute;
    right: 40px; top: 150px;
    text-align: right;
    font-size: 11px; line-height: 15px;
    color: var(--ink-soft);
  }
  .sender .line { display: flex; justify-content: flex-end; align-items: center; gap: 5px; }
  .sender svg { width: 9px; height: 9px; fill: var(--brand-red); }
  .greeting {
    position: absolute; left: 48px; top: 160px;
    font-size: 14px;
  }
  .body-copy {
    position: absolute; left: 48px; top: 228px;
    width: 580px;
    font-size: 11px; line-height: 15px;
    color: var(--ink-soft);
  }
  .body-copy p { margin-bottom: 10px; }
  .sign-off { position: absolute; left: 48px; top: 560px; }
  .sign-off .signature {
    font-family: "Cormorant Garamond", Georgia, serif;
    font-style: italic; font-size: 22px; color: var(--ink);
  }
  .sign-off .role { font-size: 12px; color: var(--ink-soft); }
  .lower-panel {
    position: absolute; left: 0; top: 625px;
    width: 520px; height: 312px;
    background: var(--panel-grey);
    overflow: hidden;
  }
  .lower-panel .faint-name {
    position: absolute; left: 20px; top: 40px;
    font-size: 240px; font-weight: 700;
    color: var(--watermark);
    letter-spacing: -6px; line-height: 1;
  }
  .footer-band {
    position: absolute; left: 0; bottom: 0;
    width: 100%; height: 25px;
    background: var(--brand-red);
    color: #fff; font-size: 10px;
    padding-left: 150px; line-height: 25px;
  }
</style>
</head>
<body>
  <main class="letterhead">
    <div class="brand-name">plomk</div>

    <address class="sender" style="font-style:normal">
      <div class="line">Your Address Goes here,</div>
      <div class="line">City, Zip code, State</div>
      <div class="line">000-000-0000 <svg viewBox="0 0 10 10"><path d="M2 0h2l1 3-1.5 1a6 6 0 0 0 2.5 2.5L7 5l3 1v2a2 2 0 0 1-2 2A8 8 0 0 1 0 2a2 2 0 0 1 2-2z"/></svg></div>
      <div class="line">000-000-0000 <svg viewBox="0 0 10 10"><path d="M2 0h2l1 3-1.5 1a6 6 0 0 0 2.5 2.5L7 5l3 1v2a2 2 0 0 1-2 2A8 8 0 0 1 0 2a2 2 0 0 1 2-2z"/></svg></div>
      <div class="line">name@domainname.com <svg viewBox="0 0 10 10"><path d="M0 2h10v6H0z M0 2l5 3.5L10 2" stroke="#fff" stroke-width=".8"/></svg></div>
    </address>

    <div class="greeting">Lorem Ipsum,</div>

    <section class="body-copy">
      <p>Duis sit amet dolor sit amet dolor tempor iaculis ac nec ante. Proin nunc diam, egestas eu semper a, fermentum ac leo. Fusce sit amet tempor elit. Mauris auctor interdum massa vitae cursus. Ut adipiscing pellentesque nunc, eget tincidunt magna imperdiet non. Curabitur eleifend elementum nisl eget iaculis. Suspendisse scelerisque ligula a nunc faucibus sit amet elementum dolor dictum.</p>
      <p>Praesent condimentum mi at ultrices fermentum. Ipsum lectus consequat mauris, ut vulputate nibh erat id eros. Vivamus ornare mattis libero at dictum. Praesent sodales metus sed nulla laoreet mollis. Curabitur non turpis in orci dignissim gravida. Aliquam tristique mauris a nibh vestibulum sagittis.</p>
      <p>Duis porta semper nibh, tincidunt aliquam metus euismod eget. Morbi varius varius pellentesque. Donec aliquam vulputate tortor non hendrerit. Suspendisse at ipsum ante, interdum porttitor ligula. Curabitur et molestie sapien. Sed magna purus, faucibus quis pulvinar nec, commodo vel justo. Nam faucibus ornare varius. Vivamus sit amet felis vitae justo scelerisque malesuada. Etiam venenatis vehicula magna, a eleifend lorem ornare nec. Maecenas eu nisl vel nunc aliquet malesuada vel in lacus.</p>
      <p>Morbi et odio eu ante pharetra iaculis vitae eget arcu. Maecenas gravida, dui vel ultricies aliquet, dui arcu luctus ante, non dignissim ipsum tortor vel orci, um fringilla mi. Mauris porta feugiat nibh et fermentum. Donec scelerisque consequat lacinia.</p>
      <p>Curabitur ac diam ut quam ultrices laoreet at ut tellus. Maecenas vitae urna in lorem condimentum sollicitudin eget vel lacus. Ut nisi turpis, tristique ullamcorper laoreet nec, gravida nec est. Donec elementum malesuada volutpat. In ac arcu quis augue vehicula fringilla.</p>
    </section>

    <div class="sign-off">
      <div class="signature">Yours name</div>
      <div class="role">Company Director</div>
    </div>

    <div class="lower-panel">
      <div class="faint-name">plomk</div>
    </div>

    <footer class="footer-band">www.websitename.com</footer>
  </main>
</body>
</html>
```